Wix Website design for my therapy business - Willowmere Group

I have started designing a Wix site and have a good idea of what I want.
I have set up the pages, created some design ideas, and inputted the copy. I need someone fabulous to finish off the design aspects. I like working closely with the designers, I was an interior designer in an old career.
I would like the site to be funky but professional. My Wix skills are limited, and I just can't achieve the look I am wanting without having to spend a lot of time learning. If it's easier to start over, that's ok providing you use the same colours, font, images etc. I have included a screenshot of the home page below. I have another site I need to start as soon as we have finished this one.
I am looking for someone who is a good listener and is has design flare. I am easy to get along with and will respond quickly.
I would like to set up SEO and have help in the future.
Let me know if you are the right person for the job.
Target Market(s)
Please needing help with their mental health and for therapy.
Industry/Entity Type
Mental health
Font styles to use
Other font styles liked:
- Futura light
Requirements
Must have
- be easy to navigate and be simple yet stylish
Nice to have
- I have set up the basics of the site - nice to haves are already on the site
Should not have
- old fashioned large chunks of text.

```html
<!DOCTYPE html>
<html lang="en">
<head>
<meta charset="utf-8">
<title>Willowmere Group – Therapy Specialists</title>
<link href="https://fonts.googleapis.com/css2?family=Hind:wght@400;500;600;700&family=Roboto:wght@400;500;700&display=swap" rel="stylesheet">
<style>
:root{
  --brown:#9a7c63;
  --brown-dark:#8a6c53;
  --heading:#94765c;
  --navy:#2b3f7c;
  --ink:#3a3a3a;
  --muted:#6b6b6b;
  --soft:#f2f2f2;
  --field:#eef3fa;
  --white:#ffffff;
  --star:#f3b321;
}
*{margin:0;padding:0;box-sizing:border-box}
html,body{width:1200px;height:4614px;overflow:hidden}
body{position:relative;background:var(--white);font-family:"Roboto",Arial,sans-serif;color:var(--ink)}
.abs{position:absolute}
h1,h2,h3,.brand{font-family:"Hind",Arial,sans-serif}

/* header */
.topbar{left:0;top:0;width:1200px;height:150px;background:#f3f7fd}
.brand{font-weight:600;color:var(--brown);font-size:34px;line-height:1;display:flex;align-items:center;gap:10px;white-space:nowrap}
.contact-item{display:flex;align-items:center;gap:12px;font-size:13px;color:var(--muted);line-height:19px}
.contact-item .ico{width:40px;height:40px;border-radius:50%;border:1px solid #d7dbe2;display:flex;align-items:center;justify-content:center}
.contact-item b{font-weight:400;color:#555;display:block}
.navbar{left:254px;top:116px;width:880px;height:50px;background:var(--white);border-radius:25px;box-shadow:0 2px 8px rgba(0,0,0,.08)}
.nav{left:88px;top:0;height:50px;display:flex;align-items:center;gap:27px;font-size:13px;color:#333}
.btn{display:flex;align-items:center;justify-content:center;background:var(--brown);color:var(--white);font-size:13px;font-weight:500}
.appointment{left:722px;top:0;width:158px;height:50px;border-radius:25px;border:3px solid #fff;box-shadow:0 0 0 2px var(--brown)}

/* hero */
.hero{left:0;top:150px;width:1200px;height:746px;background:linear-gradient(100deg,#5b4a3e 0%,#7c6a5a 40%,#a89684 70%,#7e6c5d 100%)}
.hero-label{left:82px;top:318px;color:#fff;font-size:17px;letter-spacing:.5px}
.hero-title{left:74px;top:352px;color:#fff;font-weight:500;font-size:64px;line-height:88px;width:640px}
.hero-btn{left:79px;top:639px;width:160px;height:58px;border-radius:29px}

/* about */
.about-photo-side{left:1003px;top:896px;width:197px;height:582px;background:linear-gradient(90deg,#fff 0%,#d9e4ee 40%,#7ea3c4 100%)}
.about-ring{left:94px;top:936px;width:438px;height:438px;border-radius:50%;border:2px solid var(--brown)}
.about-img{left:108px;top:950px;width:410px;height:410px;border-radius:50%;background:linear-gradient(135deg,#c8b39c,#9a8472 55%,#6d5f55)}
.about-badge{left:345px;top:1176px;width:198px;height:198px;border-radius:50%;background:var(--brown);display:flex;align-items:center;justify-content:center}
.label{font-size:11px;font-weight:700;color:var(--navy);letter-spacing:.4px;display:flex;align-items:center;gap:18px}
.label i{display:block;width:48px;height:2px;background:var(--navy)}
h2.title{font-weight:600;color:var(--heading)}
.about-title{left:634px;top:1010px;font-size:34px;line-height:46px;width:320px}
.para{font-size:12px;line-height:23px;color:#555}
.apply{border-radius:3px;height:46px}

/* services */
.services-bg{left:0;top:1478px;width:1200px;height:712px;background:var(--soft)}
.arrow-btn{width:46px;height:62px;background:#fff;border:1px solid #e3e3e3;display:flex;align-items:center;justify-content:center;border-radius:3px}
.card{top:1703px;width:321px;height:312px;border-radius:6px;overflow:hidden}
.card .pic{position:absolute;inset:0}
.card .shade{position:absolute;inset:0;background:linear-gradient(180deg,rgba(40,30,25,.15),rgba(40,30,25,.7))}
.card .ring{position:absolute;left:32px;top:42px;width:66px;height:66px;border-radius:50%;background:rgba(255,255,255,.35);border:2px solid rgba(255,255,255,.7)}
.card h3{position:absolute;left:32px;top:152px;color:#fff;font-size:22px;font-weight:600}
.card p{position:absolute;left:32px;top:210px;color:#fff;font-size:12px}
.card .more{position:absolute;left:32px;top:250px;color:#fff;font-size:14px;font-weight:700;font-family:"Hind",Arial,sans-serif}

/* cta */
.cta{left:0;top:2190px;width:1200px;height:362px;background:linear-gradient(90deg,#94765d,#a3876e 60%,#9a7c63)}
.cta-title{left:96px;top:2286px;color:#fff;font-size:44px;line-height:62px;font-weight:600;width:640px}
.cta-text{left:98px;top:2414px;color:#fff;font-size:12px;line-height:23px;width:620px}
.cta-rule{left:791px;top:2283px;width:2px;height:180px;background:#fff}
.cta-btn{left:937px;width:170px;height:46px;border-radius:4px;font-size:14px;font-weight:600;display:flex;align-items:center;justify-content:center;gap:8px}

/* gallery */
.slide{top:2751px;height:401px;border-radius:6px}
.cap{left:258px;top:3037px;width:677px;height:76px;background:#fff;display:flex;align-items:center;padding-left:40px;font-family:"Hind",Arial,sans-serif;font-size:22px;font-weight:600;color:var(--heading)}
.cap-arrow{left:856px;top:3037px;width:79px;height:76px;background:var(--brown);display:flex;align-items:center;justify-content:center}
.g-arrow{top:2912px;width:67px;height:93px;background:#fff;display:flex;align-items:center;justify-content:center}

/* testimonials */
.tcard{top:3439px;width:319px;height:229px;background:#fff;box-shadow:0 4px 18px rgba(0,0,0,.08);padding:76px 30px 0}
.avatar{width:90px;height:90px;border-radius:50%;border:5px solid #fff;background:linear-gradient(135deg,#cfd8e2,#8aa0b7);box-shadow:0 2px 8px rgba(0,0,0,.1)}
.quote{width:30px;height:30px;border-radius:50%;background:var(--brown);color:#fff;font-size:22px;font-weight:700;display:flex;align-items:center;justify-content:center;font-family:"Hind",Arial,sans-serif;padding-top:8px}
.stars{color:var(--star);font-size:17px;letter-spacing:1px}
.tcard p{font-size:12.5px;line-height:21px;color:#555;margin-top:12px}
.who{margin-top:10px;font-family:"Hind",Arial,sans-serif;font-weight:600;font-size:18px;color:var(--heading)}
.who small{font-family:"Roboto",Arial,sans-serif;font-weight:400;font-size:11px;color:#777}

/* contact */
.contact-card{left:165px;top:3872px;width:874px;height:453px;background:#fff;border-top:5px solid var(--brown);box-shadow:0 4px 20px rgba(0,0,0,.06)}
.field{left:217px;width:344px;background:var(--field);font-size:11px;color:#555;padding:14px 16px}
.info{left:645px;display:flex;gap:18px;font-size:13px;color:#333;line-height:25px}
.info .dot{width:34px;height:34px;border-radius:50%;background:var(--brown);display:flex;align-items:center;justify-content:center;flex:none}

/* footer */
.footer{left:0;top:4325px;width:1200px;height:289px;background:var(--brown)}
.f-item{display:flex;align-items:center;gap:14px;color:#fff;font-size:13px;line-height:18px}
.f-nav{left:276px;top:4490px;display:flex;gap:48px;color:#fff;font-size:13px}
.social{top:4565px;width:24px;height:24px;border:1px solid #fff;display:flex;align-items:center;justify-content:center}
</style>
</head>
<body>

<!-- HEADER -->
<div class="abs topbar"></div>
<div class="abs brand" style="left:76px;top:58px;">Willowmere Group</div>

<div class="abs contact-item" style="left:421px;top:42px;">
  <span class="ico"><svg width="16" height="16" viewBox="0 0 24 24" fill="none" stroke="#a9a9a9" stroke-width="2"><path d="M5 3h4l2 5-3 2a12 12 0 006 6l2-3 5 2v4a2 2 0 01-2 2A17 17 0 013 5a2 2 0 012-2z"/></svg></span>
  <div><b>Phone Number</b>+123 456 7890</div>
</div>
<div class="abs contact-item" style="left:666px;top:42px;">
  <span class="ico"><svg width="16" height="16" viewBox="0 0 24 24" fill="none" stroke="#a9a9a9" stroke-width="2"><rect x="3" y="5" width="18" height="14"/><path d="M3 6l9 7 9-7"/></svg></span>
  <div><b>Email Address</b>company@example.com</div>
</div>
<div class="abs contact-item" style="left:912px;top:42px;">
  <span class="ico"><svg width="16" height="16" viewBox="0 0 24 24" fill="var(--brown)"><path d="M12 2a7 7 0 00-7 7c0 5 7 13 7 13s7-8 7-13a7 7 0 00-7-7zm0 9.5A2.5 2.5 0 1112 6.5a2.5 2.5 0 010 5z"/></svg></span>
  <div><b>Location</b>123 Rd Country</div>
</div>

<!-- HERO -->
<div class="abs hero" role="img" aria-label="Photo of a smiling couple seated together on a sofa during a therapy session"></div>
<svg class="abs" style="left:0;top:780px" width="1200" height="120" viewBox="0 0 1200 120" preserveAspectRatio="none">
  <path d="M0 22 C220 70 520 118 780 116 C980 114 1110 70 1200 20 L1200 120 L0 120 Z" fill="#fff"/>
</svg>
<div class="abs hero-label">THERAPY&nbsp; SPECIALISTS</div>
<h1 class="abs hero-title">Mind, Body, Soul:<br>Holistic Healing<br>at Its Best</h1>
<div class="abs btn hero-btn">Read More</div>

<div class="abs navbar">
  <nav class="abs nav"><span>Home</span><span>About Us</span><span>Conditions</span><span>Gallery</span><span>Treatments</span><span>Contact Us</span><span>Doctors</span></nav>
  <div class="abs btn appointment">Appointment</div>
</div>

<!-- ABOUT -->
<section class="about">
  <div class="abs about-photo-side" role="img" aria-label="Photo of a smiling doctor in blue scrubs, fading into the page"></div>
  <div class="abs about-ring"></div>
  <div class="abs about-img" role="img" aria-label="Photo of a young woman talking with a therapist"></div>
  <div class="abs about-badge"><span class="brand" style="color:#fff;font-size:20px;">Willowmere Group</span></div>
  <div class="abs label" style="left:634px;top:965px;">ABOUT US <i></i></div>
  <h2 class="abs title about-title">Your Sanctuary for<br>Self-Discovery</h2>
  <p class="abs para" style="left:634px;top:1130px;width:420px;">Lorem ipsum dolor sit amet, consectetur adipiscing elit, sed do eiusmo empor incididunt ut abore et dolore magna aliqua. Ut enim ad minim iam, quis nostrud exercitation ullamco</p>
  <p class="abs para" style="left:634px;top:1213px;width:420px;">Lorem ipsum dolor sit amet, consectetur adipiscing elit, sed do eiusmo empor incididunt ut abore et dolore magna aliqua. Ut enim ad minim iam, quis nostrud exercitation ullamco</p>
  <div class="abs btn apply" style="left:634px;top:1320px;width:168px;">Apply Now</div>
</section>

<!-- SERVICES -->
<div class="abs services-bg"></div>
<div class="abs label" style="left:90px;top:1564px;">SERVICES <i></i></div>
<h2 class="abs title" style="left:88px;top:1598px;font-size:45px;">Services We Offer</h2>
<div class="abs arrow-btn" style="left:999px;top:1580px;"><svg width="10" height="16" viewBox="0 0 10 16" fill="none" stroke="#333" stroke-width="1.6"><path d="M8 2L2 8l6 6"/></svg></div>
<div class="abs arrow-btn" style="left:1051px;top:1580px;"><svg width="10" height="16" viewBox="0 0 10 16" fill="none" stroke="#333" stroke-width="1.6"><path d="M2 2l6 6-6 6"/></svg></div>

<div class="abs card" style="left:91px;">
  <div class="pic" role="img" aria-label="Photo of a thoughtful woman in a green jacket" style="background:linear-gradient(135deg,#b89a82,#6e5a4c 60%,#4f4640)"></div>
  <div class="shade"></div><div class="ring"></div>
  <h3 style="top:158px;">Addictions</h3>
  <p>Lorem ipsum dolor sit amet, consectetur</p>
  <div class="more">Read More</div>
</div>
<div class="abs card" style="left:439px;">
  <div class="pic" role="img" aria-label="Photo of a woman in a striped top speaking with a counselor" style="background:linear-gradient(135deg,#c9c1b8,#8d8178 60%,#5d544e)"></div>
  <div class="shade"></div><div class="ring"></div>
  <h3 style="top:146px;">Betrayal Trauma</h3>
  <p>Lorem ipsum dolor sit amet, consectetur</p>
  <div class="more">Read More</div>
</div>
<div class="abs card" style="left:788px;">
  <div class="pic" role="img" aria-label="Photo of a man in a jacket during a counseling session" style="background:linear-gradient(135deg,#7f6f68,#5a3f3a 55%,#3c3534)"></div>
  <div class="shade"></div><div class="ring"></div>
  <h3 style="top:146px;">PTSD</h3>
  <p>Lorem ipsum dolor sit amet, consectetur</p>
  <div class="more">Read More</div>
</div>
<div class="abs btn apply" style="left:514px;top:2087px;width:167px;height:48px;">Apply Now</div>

<!-- CTA -->
<div class="abs cta" role="img" aria-label="Soft brown band with a faint photo of a therapy session"></div>
<h2 class="abs cta-title">Get in touch with us for<br>therapy care</h2>
<p class="abs cta-text">Lorem ipsum dolor sit amet, consectetur adipiscing elit, sed do eiusmoempor incididunt ut abore et dolore magna aliqua. Ut enim ad minim iam</p>
<div class="abs cta-rule"></div>
<svg class="abs" style="left:792px;top:2366px" width="8" height="14" viewBox="0 0 8 14"><path d="M0 0l8 7-8 7z" fill="#fff"/></svg>
<div class="abs cta-btn" style="top:2318px;border:2px solid #fff;color:#fff;">
  <svg width="14" height="14" viewBox="0 0 24 24" fill="#fff"><path d="M5 3h4l2 5-3 2a12 12 0 006 6l2-3 5 2v4a2 2 0 01-2 2A17 17 0 013 5a2 2 0 012-2z"/></svg>+123 456 789</div>
<div class="abs cta-btn" style="top:2384px;background:#fff;color:var(--brown);font-size:13px;">Contact Us</div>

<!-- GALLERY -->
<div class="abs label" style="left:516px;top:2611px;"><i></i>GALLERY<i></i></div>
<h2 class="abs title" style="left:0;top:2636px;width:1212px;text-align:center;font-size:45px;">Why Choose Us</h2>
<div class="abs slide" style="left:0;width:179px;border-radius:0 6px 6px 0;background:linear-gradient(135deg,#8f8a86,#56606b)" role="img" aria-label="Photo of a man seated in a counseling session"></div>
<div class="abs slide" style="left:218px;width:756px;background:linear-gradient(120deg,#cdbca8,#e8ddd0 45%,#b5a392 80%,#8a7868)" role="img" aria-label="Photo of a therapist holding emotion cards with a young child"></div>
<div class="abs slide" style="left:1012px;width:188px;border-radius:6px 0 0 6px;background:linear-gradient(135deg,#d9cfc6,#8c7566)" role="img" aria-label="Photo of a woman talking in a bright room"></div>
<div class="abs g-arrow" style="left:91px;"><svg width="12" height="22" viewBox="0 0 12 22" fill="none" stroke="#333" stroke-width="1.8"><path d="M10 2L2 11l8 9"/></svg></div>
<div class="abs g-arrow" style="left:1035px;"><svg width="12" height="22" viewBox="0 0 12 22" fill="none" stroke="#333" stroke-width="1.8"><path d="M2 2l8 9-8 9"/></svg></div>
<div class="abs cap">Client Centered</div>
<div class="abs cap-arrow"><svg width="30" height="14" viewBox="0 0 30 14" fill="none" stroke="#fff" stroke-width="1.6"><path d="M0 7h28M22 1l6 6-6 6"/></svg></div>

<!-- TESTIMONIALS -->
<div class="abs label" style="left:90px;top:3274px;">TESTIMONIALS <i></i></div>
<h2 class="abs title" style="left:88px;top:3308px;font-size:45px;">What our clients are saying</h2>
<div class="abs arrow-btn" style="left:999px;top:3290px;"><svg width="10" height="16" viewBox="0 0 10 16" fill="none" stroke="#333" stroke-width="1.6"><path d="M8 2L2 8l6 6"/></svg></div>
<div class="abs arrow-btn" style="left:1051px;top:3290px;"><svg width="10" height="16" viewBox="0 0 10 16" fill="none" stroke="#333" stroke-width="1.6"><path d="M2 2l6 6-6 6"/></svg></div>

<div class="abs tcard" style="left:93px;"><div class="stars">★★★★★</div><p>Lorem ipsum dolor sit amet, consectetur adipiscing elit, sed do eiusmod tempor in cididunt ut labore et dolore magna a iqua. Ut enim ad</p><div class="who">Elias Brandt <small>(Client)</small></div></div>
<div class="abs tcard" style="left:437px;"><div class="stars">★★★★★</div><p>Lorem ipsum dolor sit amet, consectetur adipiscing elit, sed do eiusmod tempor in cididunt ut labore et dolore magna a iqua. Ut enim ad</p><div class="who">Elias Brandt <small>(Client)</small></div></div>
<div class="abs tcard" style="left:783px;"><div class="stars">★★★★★</div><p>Lorem ipsum dolor sit amet, consectetur adipiscing elit, sed do eiusmod tempor in cididunt ut labore et dolore magna a iqua. Ut enim ad</p><div class="who">Elias Brandt <small>(Client)</small></div></div>

<div class="abs avatar" style="left:293px;top:3405px;" role="img" aria-label="Client portrait"></div>
<div class="abs quote" style="left:355px;top:3408px;">”</div>
<div class="abs avatar" style="left:637px;top:3405px;" role="img" aria-label="Client portrait"></div>
<div class="abs quote" style="left:699px;top:3408px;">”</div>
<div class="abs avatar" style="left:983px;top:3405px;" role="img" aria-label="Client portrait"></div>
<div class="abs quote" style="left:1045px;top:3408px;">”</div>

<div class="abs" style="left:554px;top:3702px;width:34px;height:5px;background:var(--navy);border-radius:3px"></div>
<div class="abs" style="left:596px;top:3702px;width:18px;height:5px;background:#ddd;border-radius:3px"></div>
<div class="abs" style="left:620px;top:3702px;width:18px;height:5px;background:#ddd;border-radius:3px"></div>

<!-- CONTACT -->
<div class="abs label" style="left:516px;top:3761px;"><i></i>CONTACT<i></i></div>
<h2 class="abs title" style="left:0;top:3788px;width:1212px;text-align:center;font-size:45px;">Get in touch with us</h2>
<svg class="abs" style="left:0;top:4060px" width="1200" height="270" viewBox="0 0 1200 270" preserveAspectRatio="none">
  <path d="M0 60 C60 40 120 20 165 15 L165 270 L0 270Z" fill="var(--brown)"/>
  <path d="M1039 135 C1100 110 1160 100 1200 95 L1200 270 L1039 270Z" fill="var(--brown)"/>
</svg>
<div class="abs contact-card"></div>
<h2 class="abs title" style="left:217px;top:3912px;font-size:31px;line-height:36px;">Feel free to write us<br>for any type of</h2>
<div class="abs field" style="top:4006px;height:44px;">Full Name</div>
<div class="abs field" style="top:4060px;height:43px;">Enter Email address</div>
<div class="abs field" style="top:4114px;height:72px;">Your Messages</div>
<div class="abs btn" style="left:217px;top:4205px;width:188px;height:47px;font-size:15px;font-weight:700;">SUBMIT NOW</div>
<div class="abs" style="left:618px;top:3895px;width:1px;height:405px;background:#e4e4e4"></div>

<div class="abs info" style="top:3925px;"><span class="dot"><svg width="14" height="14" viewBox="0 0 24 24" fill="#fff"><path d="M12 2a7 7 0 00-7 7c0 5 7 13 7 13s7-8 7-13a7 7 0 00-7-7z"/></svg></span><div>Company Name<br>ABC Road<br>ABC City<br>ABC Country</div></div>
<div class="abs info" style="top:4043px;"><span class="dot"><svg width="14" height="14" viewBox="0 0 24 24" fill="#fff"><path d="M5 3h4l2 5-3 2a12 12 0 006 6l2-3 5 2v4a2 2 0 01-2 2A17 17 0 013 5a2 2 0 012-2z"/></svg></span><div style="padding-top:4px">123 - 456 - 7890</div></div>
<div class="abs info" style="top:4098px;"><span class="dot"><svg width="14" height="14" viewBox="0 0 24 24" fill="none" stroke="#fff" stroke-width="2.2"><rect x="3" y="5" width="18" height="14"/><path d="M3 6l9 7 9-7"/></svg></span><div style="padding-top:4px">contactus@company.com</div></div>
<div class="abs info" style="top:4151px;"><span class="dot"><svg width="14" height="14" viewBox="0 0 24 24" fill="#fff"><path d="M3 5l9 7-9 7zM12 5l9 7-9 7z"/></svg></span><div style="padding-top:4px">8 am - 5pm&nbsp; Mon - Fri</div></div>
<div class="abs" style="left:656px;top:4222px;font-size:13px;color:#333;">Reach us here:</div>

<!-- FOOTER -->
<div class="abs footer"></div>
<div class="abs brand" style="left:184px;top:4394px;color:#fff;font-size:24px;">Willowmere Group</div>
<div class="abs" style="left:412px;top:4385px;width:1px;height:46px;background:rgba(255,255,255,.5)"></div>
<div class="abs f-item" style="left:430px;top:4390px;">
  <svg width="30" height="30" viewBox="0 0 24 24" fill="none" stroke="#fff" stroke-width="1.3"><circle cx="12" cy="12" r="9"/><path d="M3 12h18M12 3c3 3 3 15 0 18M12 3c-3 3-3 15 0 18"/></svg>
  <div>123, Building Name, Street<br>City, State XY 123456</div></div>
<div class="abs" style="left:668px;top:4385px;width:1px;height:46px;background:rgba(255,255,255,.5)"></div>
<div class="abs f-item" style="left:686px;top:4390px;">
  <svg width="24" height="30" viewBox="0 0 24 30" fill="none" stroke="#fff" stroke-width="1.4"><rect x="4" y="2" width="14" height="26" rx="2"/><path d="M9 24h4"/></svg>
  <div>PHONE<br>(123) 456 7890</div></div>
<div class="abs" style="left:845px;top:4385px;width:1px;height:46px;background:rgba(255,255,255,.5)"></div>
<div class="abs f-item" style="left:863px;top:4390px;">
  <svg width="28" height="28" viewBox="0 0 24 24" fill="none" stroke="#fff" stroke-width="1.3"><path d="M3 10l9-6 9 6v10H3z"/><path d="M3 10l9 6 9-6"/></svg>
  <div>EMAIL<br>info@company.com</div></div>
<div class="abs" style="left:184px;top:4462px;width:860px;height:1px;background:rgba(255,255,255,.35)"></div>
<nav class="abs f-nav"><span>HOME</span><span>SERVICES</span><span>ABOUT US</span><span>TESTIMONIALS</span><span>BLOG</span><span>CONTACT US</span></nav>
<div class="abs" style="left:148px;top:4570px;font-size:11px;color:rgba(255,255,255,.55);">All Rights Reserved. 2023</div>
<div class="abs social" style="left:933px;"></div>
<div class="abs social" style="left:966px;"></div>
<div class="abs social" style="left:1000px;"></div>
<div class="abs social" style="left:1034px;"></div>

</body>
</html>
```